WordPress Website for Pain Relief Clinic

I need a WordPress website designed for my laser pain relief clinic. It needs to be a professional, responsive design with 7 pages: Home, Why Choose Us, Treatable Conditions, Testimonials, FAQ, Franchising, Contact Us. Here is logo: https://files.brivoltcdn.com/media.t-w-e-n.com/sitebuilder/472/CalvexaLogoHighQuality.png

Target Market(s)

people with pain,elderly adults,injuries,soreness

Industry/Entity Type

Clinic

Number of Pages Required

5+ page

Colors
0792cd
85abd2

```html
<!DOCTYPE html>
<html lang="en">
<head>
<meta charset="utf-8">
<title>Calvexa Pain Treatment Centre</title>
<link href="https://fonts.googleapis.com/css2?family=Roboto:wght@300;400;500;700&display=swap" rel="stylesheet">
<style>
:root{
  --blue:#0792cd;
  --blue-dark:#0a6fa3;
  --sky:#85abd2;
  --red:#c8161d;
  --red-dark:#a81117;
  --ink:#333;
  --muted:#666;
  --grey:#e9e9e9;
  --footer:#1c1c1c;
  --footer-deep:#111;
}
*{box-sizing:border-box;margin:0;padding:0}
html,body{width:678px;height:1200px;overflow:hidden}
body{font-family:'Roboto',Arial,sans-serif;color:var(--ink);background:#fff;font-size:11px}
.site{width:678px;height:1200px;position:relative}

.header{height:86px;display:flex;justify-content:space-between;align-items:center;padding:0 24px}
.brand{display:flex;align-items:center;gap:10px}
.brand-mark{width:14px;height:14px;border-radius:50%;background:var(--blue)}
.brand-name{font-size:34px;font-weight:700;color:var(--blue);letter-spacing:.5px}
.contact-top{display:flex;flex-direction:column;gap:8px}
.contact-top .item{display:flex;align-items:center;gap:8px;color:var(--ink)}
.contact-top .phone{font-size:17px}
.contact-top .mail{font-size:10px}
.ic{width:20px;height:20px;border-radius:50%;background:var(--blue);display:flex;align-items:center;justify-content:center;flex:none}

.nav{height:32px;background:var(--blue);display:flex;padding-left:18px}
.nav a{color:#fff;text-decoration:none;font-size:11px;padding:0 12px;line-height:32px}
.nav a.active{background:var(--blue-dark)}

.hero{height:270px;position:relative;background:linear-gradient(180deg,#f4f4f4,#d9d9d9)}
.hero-photo{position:absolute;left:16px;top:10px;width:250px;height:250px;border-radius:50%;border:6px solid #fff;background:radial-gradient(circle at 50% 40%,#d9a992 0%,#b07e6a 45%,#5a5a5a 100%)}
.hero-text{position:absolute;right:24px;top:38px;width:260px;text-align:right}
.hero-text h1{font-weight:300;font-size:30px;line-height:36px;color:#222}
.hero-text p{text-align:left;font-size:9px;line-height:13px;color:var(--muted);margin:10px 0 14px}
.btn{display:inline-block;border:2px solid var(--blue);color:var(--blue);font-size:11px;padding:7px 12px;border-radius:3px;background:#fff}
.dots{position:absolute;left:290px;bottom:10px;display:flex;gap:6px}
.dots span{width:11px;height:11px;border-radius:50%;background:#bbb;border:2px solid #fff}
.dots span.on{background:var(--blue)}

.cta{height:60px;background:var(--blue);color:#fff;font-size:24px;font-weight:300;display:flex;align-items:center;justify-content:center}

.why{height:276px;position:relative;padding:26px 24px 0}
.why h2{text-align:center;font-weight:300;font-size:30px;color:var(--blue)}
.why-copy{position:absolute;left:60px;top:88px;width:250px}
.why-copy p{font-size:9px;line-height:13px;color:var(--muted);margin-bottom:14px}
.bubble{position:absolute;border-radius:50%;background:var(--blue);border:3px solid #fff;box-shadow:0 0 0 2px var(--blue);color:#fff;display:flex;align-items:center;justify-content:center;text-align:center;font-size:19px;line-height:22px}
.b1{left:420px;top:80px;width:90px;height:90px}
.b2{left:505px;top:102px;width:100px;height:100px}
.b3{left:440px;top:160px;width:90px;height:90px}

.split{height:230px;display:flex;gap:20px;padding:0 60px 0 60px}
.testimonial{flex:1;background:var(--grey);border-top:4px solid #ccc;padding:16px 30px;text-align:center;height:210px}
.testimonial h3{font-weight:400;font-size:21px;color:#222}
.quote{font-size:30px;color:#444;line-height:26px;margin-top:6px;font-family:Georgia,serif}
.testimonial p{font-size:9px;line-height:13px;color:var(--muted)}
.testimonial .who{font-weight:700;color:#222;margin-top:10px}
.tdots{display:flex;gap:5px;justify-content:center;margin-top:10px}
.tdots span{width:10px;height:10px;border-radius:50%;background:#bbb}
.tdots span.on{background:var(--blue)}
.hours{width:176px;background:var(--red);color:#fff;text-align:center;padding:14px 12px;height:200px;border-bottom:4px solid var(--red-dark)}
.clock{width:28px;height:28px;margin:0 auto}
.hours h3{font-size:15px;font-weight:700;margin:8px 0 8px}
.hours li{list-style:none;font-size:8.5px;line-height:16px;text-align:left;padding-left:14px}

.newsletter{height:124px;background:var(--blue);color:#fff;text-align:center;padding-top:18px;margin-top:2px}
.newsletter h2{font-weight:300;font-size:28px}
.newsletter p{font-size:9px;margin:4px 0 12px}
.form{display:flex;justify-content:center;gap:12px}
.field{width:170px;height:24px;background:#fff;color:#999;font-size:9px;text-align:left;padding:6px 8px}
.submit{width:86px;height:24px;background:var(--footer);color:#fff;font-size:12px;line-height:24px}

.foot-nav{height:44px;background:var(--footer);display:flex;align-items:center;padding:0 24px;gap:14px}
.foot-nav a{color:#fff;text-decoration:none;font-size:10px}
.foot-nav a.active{border:1px solid #fff;border-radius:12px;padding:3px 10px}
.social{margin-left:auto;display:flex;gap:12px}
.social span{width:10px;height:10px;border-radius:50%;background:#fff}
.foot-info{height:54px;background:var(--footer);display:flex;align-items:center;justify-content:space-between;padding:0 24px;color:#fff;font-size:10px}
.foot-info .item{display:flex;align-items:center;gap:8px}
.copy{height:22px;background:var(--footer-deep);color:#fff;text-align:center;font-size:9px;line-height:22px}
.copy b{color:var(--blue);font-weight:400}
</style>
</head>
<body>
<div class="site">
  <header class="header">
    <div class="brand"><span class="brand-mark"></span><span class="brand-name">Calvexa</span></div>
    <div class="contact-top">
      <div class="item phone"><span class="ic"><svg width="11" height="11" viewBox="0 0 24 24"><path fill="#fff" d="M6.6 10.8a15 15 0 0 0 6.6 6.6l2.2-2.2c.3-.3.7-.4 1-.2 1.1.4 2.3.6 3.6.6.6 0 1 .4 1 1V20c0 .6-.4 1-1 1A17 17 0 0 1 3 4c0-.6.4-1 1-1h3.5c.6 0 1 .4 1 1 0 1.3.2 2.5.6 3.6.1.3 0 .7-.2 1z"/></svg></span>123 456 7890</div>
      <div class="item mail"><span class="ic"><svg width="11" height="11" viewBox="0 0 24 24"><path fill="#fff" d="M3 5h18v14H3z"/><path fill="none" stroke="#0792cd" stroke-width="2" d="M3 6l9 7 9-7"/></svg></span>info@calvexapaincare.com</div>
    </div>
  </header>

  <nav class="nav">
    <a class="active">Home</a><a>Why Choose Us</a><a>Treatable Conditions</a><a>Testimonials</a><a>FAQ</a><a>Franchising</a><a>Contact Us</a>
  </nav>

  <section class="hero">
    <div class="hero-photo" role="img" aria-label="Photo of a man's bare back with a highlighted sore spot on the neck and shoulder"></div>
    <div class="hero-text">
      <h1>Recover with<br>Laser Solutions</h1>
      <p>Lorem Ipsum is simply dummy text of the printing and typesetting industry. Lorem Ipsum has been the industry's standard dummy text ever since the 1500s.</p>
      <span class="btn">READ MORE</span>
    </div>
    <div class="dots"><span class="on"></span><span></span><span></span></div>
  </section>

  <section class="cta">Start Living Pain Free Today Call Us - 123 456 7890</section>

  <section class="why">
    <h2>Why Choose Us</h2>
    <div class="why-copy">
      <p>Lorem Ipsum is simply dummy text of the printing and typesetting industry. Lorem Ipsum has been the industry's standard dummy text ever since the 1500s, when an unknown printer took a galley of type and scrambled it to make a type specimen book. It has survived not only five centuries.</p>
      <p>Lorem Ipsum is simply dummy text of the printing and typesetting industry. Lorem Ipsum has been the industry's standard dummy text ever since the 1500s.</p>
      <span class="btn">READ MORE</span>
    </div>
    <div class="bubble b1">No<br>Pain</div>
    <div class="bubble b2">No<br>Drugs</div>
    <div class="bubble b3">No<br>Surgery</div>
  </section>

  <section class="split">
    <div class="testimonial">
      <h3>Our Client Say</h3>
      <div class="quote">&ldquo;</div>
      <p>Lorem Ipsum is simply dummy text of the printing and typesetting industry. Lorem Ipsum has been the industry's standard dummy text ever since the 1500s, when an unknown printer took a galley of type and scrambled it to make a type specimen book. It has survived not only five centuries.</p>
      <p class="who">- Client Name</p>
      <div class="tdots"><span class="on"></span><span></span><span></span></div>
    </div>
    <div class="hours">
      <svg class="clock" viewBox="0 0 28 28"><circle cx="14" cy="14" r="13" fill="#fff"/><path d="M14 6v8l5 3" fill="none" stroke="#c8161d" stroke-width="2.5" stroke-linecap="round"/></svg>
      <h3>Opening Hours</h3>
      <ul>
        <li>Mon : 8:00 am to 12:30 Pm</li>
        <li>Tue : 8:00 am to 12:30 Pm</li>
        <li>Wed : 8:00 am to 12:30 Pm</li>
        <li>Thu : 8:00 am to 12:30 Pm</li>
        <li>Fri : 8:00 am to 12:30 Pm</li>
        <li>Sat : 8:00 am to 12:30 Pm</li>
        <li>Sun : Free Day</li>
      </ul>
    </div>
  </section>

  <section class="newsletter">
    <h2>Newsletter</h2>
    <p>Lorem Ipsum is simply dummy text - Subscribe to Healthcare Prodating</p>
    <div class="form"><div class="field">Enter Name</div><div class="field">Enter Mail</div><div class="submit">Subscribe</div></div>
  </section>

  <nav class="foot-nav">
    <a class="active">Home</a><a>Why Choose Us</a><a>Treatable Conditions</a><a>Testimonials</a><a>FAQ</a><a>Franchising</a><a>Contact Us</a>
    <div class="social"><span></span><span></span><span></span></div>
  </nav>

  <section class="foot-info">
    <div class="item"><span class="ic"><svg width="11" height="11" viewBox="0 0 24 24"><path fill="#fff" d="M12 2a7 7 0 0 0-7 7c0 5 7 13 7 13s7-8 7-13a7 7 0 0 0-7-7zm0 9.5A2.5 2.5 0 1 1 12 6.5a2.5 2.5 0 0 1 0 5z"/></svg></span>Lorem Ipsum is simply dummy text<br>of the printing and type</div>
    <div class="item"><span class="ic"><svg width="11" height="11" viewBox="0 0 24 24"><path fill="#fff" d="M6.6 10.8a15 15 0 0 0 6.6 6.6l2.2-2.2c.3-.3.7-.4 1-.2 1.1.4 2.3.6 3.6.6.6 0 1 .4 1 1V20c0 .6-.4 1-1 1A17 17 0 0 1 3 4c0-.6.4-1 1-1h3.5c.6 0 1 .4 1 1 0 1.3.2 2.5.6 3.6.1.3 0 .7-.2 1z"/></svg></span>123 456 7890</div>
    <div class="item"><span class="ic"><svg width="11" height="11" viewBox="0 0 24 24"><path fill="#fff" d="M3 5h18v14H3z"/><path fill="none" stroke="#0792cd" stroke-width="2" d="M3 6l9 7 9-7"/></svg></span>info@calvexapaincare.com</div>
  </section>

  <div class="copy">&copy; <b>Calvexa Pain Treatment Centre</b> - 2015. All Rights Reserved</div>
</div>
</body>
</html>
```